UX Design for Analytics Web Application

http://tovelunigroup.com/
We are tech & consulting company with analytics products (web applications), located at Rio de Janeiro, Brazil.

We are searching a partner do develop UX for our products, i.e, aesthetics, usability, HTML/CSS.

Currently we have a product suite and the goal is to make a pilot re-design project with one of our products.

The product of interest is interactive webapp that aims at data analysis, significantly different from blogs, e-commerce or landing pages.

We do have a software development team but we lack an UX & HTML expert. Currently we use Bootstrap templates but the results are insatisfatory.

So, the project scope is, to develop the arts (UX, aesthetics, etc) along with the code/mockup (HTML/CSS) for one of our product (3 pages).

This is a pilot project and there's potential to rehire for our other products. Code quality is of importance.

More details and specification can be found in attached files.

Target Market(s)

Executives, managers & consultants

Industry/Entity Type

It Company

Coding

Coded - Design and coding required

Number of Pages Required

3 page

Font styles to use
Sans Serif

Requirements
Must have
• (see attached files, prefer the pptx version))
• -Responsive
Nice to have
• (see attached files, prefer the pptx version)
Should not have
• -Avoid Green, Red and Yellow colors. They have a meaning of good, bad and average in our products.

```html
<!DOCTYPE html>
<html lang="en">
<head>
<meta charset="utf-8">
<title>Tovelu — Process Dashboard</title>
<link rel="stylesheet" href="https://fonts.googleapis.com/css2?family=Open+Sans:wght@300;400;600&family=Oswald:wght@400&display=swap">
<style>
  :root {
    --ink: #3f3f3f;
    --ink-soft: #555;
    --muted: #8a8a8a;
    --rule: #e2e2e2;
    --panel: #4a4a4a;
    --panel-text: #c9c9c9;
    --accent-ring: #5cb8f0;
    --ring-track: #8d8d8d;
    --title: #1d5f9e;
    --value: #2f86c9;
    --bar-fill: #2f86c9;
    --bar-track: #e3e3e3;
    --badge: #2f86c9;
    --card-bg: #f7f7f7;
    --tile-bg: #f3f3f3;
    --footer-bg: #ebebeb;
    --white: #fff;
  }
  * { box-sizing: border-box; margin: 0; padding: 0; }
  html, body { width: 1200px; height: 1160px; overflow: hidden; }
  body { position: relative; background: var(--white); font-family: "Open Sans", Arial, sans-serif; color: var(--ink); }

  .site-header { position: absolute; left: 0; top: 0; width: 1200px; height: 128px; border-bottom: 1px solid var(--rule); }
  .menu-toggle { position: absolute; left: 24px; top: 52px; width: 28px; display: flex; flex-direction: column; gap: 5px; }
  .menu-toggle span { display: block; height: 4px; background: var(--ink); border-radius: 1px; }
  .brand { position: absolute; left: 132px; top: 30px; display: flex; align-items: center; gap: 12px; }
  .brand-dot { width: 46px; height: 46px; border-radius: 50%; background: var(--ink); }
  .brand-name { font-size: 44px; font-weight: 600; color: var(--ink); letter-spacing: 1px; line-height: 1; }
  .header-actions { position: absolute; top: 44px; left: 883px; display: flex; gap: 32px; }
  .icon-btn { position: relative; width: 40px; height: 40px; border-radius: 50%; background: var(--ink); display: flex; align-items: center; justify-content: center; }
  .icon-btn svg { width: 18px; height: 18px; fill: var(--white); }
  .badge { position: absolute; left: -9px; top: -2px; width: 18px; height: 18px; border-radius: 50%; background: var(--badge); color: var(--white); font-size: 9px; line-height: 18px; text-align: center; }

  .summary { position: absolute; left: 132px; top: 146px; width: 936px; height: 224px; background: var(--panel); }
  .stat { position: absolute; top: 32px; width: 160px; text-align: center; }
  .stat svg { display: block; margin: 0 auto; width: 114px; height: 114px; }
  .stat-value { font-family: "Oswald", "Arial Narrow", sans-serif; font-size: 46px; fill: var(--accent-ring); }
  .stat-label { margin-top: 10px; font-size: 15px; font-weight: 300; line-height: 20px; color: var(--panel-text); }
  .stat.active { left: 11px; }
  .stat.done { left: 200px; }
  .stat.rate { left: 388px; }

  .tile { position: absolute; top: 32px; width: 150px; height: 157px; background: var(--tile-bg); padding: 12px 10px 0 11px; }
  .profile { left: 582px; }
  .profile-name { font-size: 15px; font-weight: 600; color: var(--ink); line-height: 20px; }
  .profile-date { font-size: 10px; color: var(--ink-soft); margin-top: 1px; }
  .profile-note { margin-top: 12px; font-size: 8.2px; line-height: 14.4px; color: var(--muted); text-align: justify; }
  .totals { left: 770px; }
  .total + .total { margin-top: 14px; }
  .total-amount { font-size: 14px; font-weight: 600; color: var(--ink); line-height: 18px; }
  .total-label { font-size: 10px; color: var(--ink-soft); line-height: 13px; }

  .toolbar { position: absolute; left: 132px; top: 401px; width: 936px; height: 36px; }
  .sort-label { position: absolute; left: 0; top: 10px; font-size: 11.5px; color: var(--ink); }
  .select { position: absolute; left: 51px; top: 0; width: 160px; height: 36px; border: 1px solid #cfcfcf; border-radius: 2px; font-size: 11.5px; padding: 10px 10px; }
  .select svg { position: absolute; right: 12px; top: 14px; width: 9px; height: 6px; fill: none; stroke: var(--ink); stroke-width: 1.4; }
  .btn { position: absolute; top: 0; height: 36px; border: 1px solid #cfcfcf; border-radius: 2px; font-size: 11.5px; display: flex; align-items: center; justify-content: center; gap: 7px; background: var(--white); }
  .btn svg { width: 12px; height: 12px; }
  .btn-add { left: 687px; width: 112px; }
  .btn-delete { left: 807px; width: 129px; }

  .process-grid { position: absolute; left: 132px; top: 470px; width: 937px; display: grid; grid-template-columns: repeat(3, 298px); column-gap: 21.5px; row-gap: 22px; }
  .process-card { height: 283px; background: var(--card-bg); box-shadow: 0 0 3px rgba(0,0,0,.16); padding: 26px 13px 0 13px; }
  .process-title { padding-left: 10px; font-size: 16.5px; font-weight: 400; color: var(--title); line-height: 22px; }
  .process-value { padding-left: 10px; font-size: 14px; color: var(--value); line-height: 20px; margin-top: 2px; }
  .progress { margin: 15px 10px 0 10px; height: 10px; background: var(--bar-track); }
  .progress-fill { width: 81%; height: 100%; background: var(--bar-fill); }
  .process-desc { margin: 22px 10px 0 10px; font-size: 9px; line-height: 16px; color: var(--muted); text-align: justify; }
  .process-step { margin-top: 13px; height: 58px; background: var(--white); padding: 9px 12px; }
  .step-label { font-size: 13px; font-weight: 300; color: var(--ink); line-height: 16px; }
  .step-name { font-size: 16.5px; color: #222; line-height: 24px; }

  .site-footer { position: absolute; left: 0; top: 1104px; width: 1200px; height: 56px; background: var(--footer-bg); text-align: center; font-size: 10.5px; padding-top: 21px; color: var(--ink); }
</style>
</head>
<body>
  <header class="site-header">
    <div class="menu-toggle" aria-label="Menu"><span></span><span></span><span></span></div>
    <div class="brand"><span class="brand-dot"></span><span class="brand-name">Tovelu</span></div>
    <div class="header-actions">
      <div class="icon-btn" aria-label="Notifications">
        <span class="badge">0</span>
        <svg viewBox="0 0 24 24"><path d="M12 22a2.5 2.5 0 0 0 2.5-2.5h-5A2.5 2.5 0 0 0 12 22zm7-6V11c0-3.3-2.2-6-5.2-6.8V3.5a1.8 1.8 0 0 0-3.6 0v.7C7.2 5 5 7.7 5 11v5l-2 2v1h18v-1z"/></svg>
      </div>
      <div class="icon-btn" aria-label="Profile">
        <svg viewBox="0 0 24 24"><circle cx="12" cy="7.5" r="4.5"/><path d="M3.5 21c0-4.4 3.8-7.5 8.5-7.5s8.5 3.1 8.5 7.5z"/></svg>
      </div>
      <div class="icon-btn" aria-label="Settings">
        <svg viewBox="0 0 24 24"><path d="M19.4 13a7.5 7.5 0 0 0 0-2l2.1-1.6-2-3.5-2.5 1a7.3 7.3 0 0 0-1.7-1L15 3h-4l-.4 2.9a7.3 7.3 0 0 0-1.7 1l-2.5-1-2 3.5L6.6 11a7.5 7.5 0 0 0 0 2l-2.1 1.6 2 3.5 2.5-1a7.3 7.3 0 0 0 1.7 1L11 21h4l.4-2.9a7.3 7.3 0 0 0 1.7-1l2.5 1 2-3.5zM13 15.5a3.5 3.5 0 1 1 0-7 3.5 3.5 0 0 1 0 7z" transform="translate(-1 0)"/></svg>
      </div>
    </div>
  </header>

  <section class="summary">
    <div class="stat active">
      <svg viewBox="0 0 114 114"><circle cx="57" cy="57" r="55" fill="none" stroke="var(--accent-ring)" stroke-width="3"/><text class="stat-value" x="57" y="75" text-anchor="middle">82</text></svg>
      <div class="stat-label">Number of<br>active processes</div>
    </div>
    <div class="stat done">
      <svg viewBox="0 0 114 114"><circle cx="57" cy="57" r="55" fill="none" stroke="var(--accent-ring)" stroke-width="3"/><text class="stat-value" x="57" y="75" text-anchor="middle">79</text></svg>
      <div class="stat-label">Number of<br>completed processes</div>
    </div>
    <div class="stat rate">
      <svg viewBox="0 0 114 114">
        <circle cx="57" cy="57" r="55" fill="none" stroke="var(--ring-track)" stroke-width="3"/>
        <circle cx="57" cy="57" r="55" fill="none" stroke="var(--accent-ring)" stroke-width="3" stroke-dasharray="248.8 345.6" transform="rotate(-90 57 57)"/>
        <text class="stat-value" x="57" y="75" text-anchor="middle">72%</text>
      </svg>
      <div class="stat-label">Completion</div>
    </div>
    <div class="tile profile">
      <div class="profile-name">Lena Hart</div>
      <div class="profile-date">Feb, 2017</div>
      <p class="profile-note">Integer feugiat id purus nec sodales. Nulla ate tincidunt elementum nisl, sed dignissim vitae ipsum ornare vel. Aenean ate lectus viverra, venenatis lectus</p>
    </div>
    <div class="tile totals">
      <div class="total"><div class="total-amount">$00.00</div><div class="total-label">Sed ante justo</div></div>
      <div class="total"><div class="total-amount">$00.00</div><div class="total-label">Donec vestibulum tempus</div></div>
      <div class="total"><div class="total-amount">$00.00</div><div class="total-label">Nullam ornare tortor</div></div>
    </div>
  </section>

  <div class="toolbar">
    <span class="sort-label">Sort by :</span>
    <div class="select">Latest Process<svg viewBox="0 0 9 6"><path d="M1 1l3.5 3.5L8 1"/></svg></div>
    <div class="btn btn-add"><svg viewBox="0 0 12 12"><circle cx="6" cy="6" r="6" fill="#666"/><path d="M6 3v6M3 6h6" stroke="#fff" stroke-width="1.5"/></svg>Add Process</div>
    <div class="btn btn-delete"><svg viewBox="0 0 12 12"><circle cx="6" cy="6" r="6" fill="#666"/><path d="M3 6h6" stroke="#fff" stroke-width="1.5"/></svg>Delete Process</div>
  </div>

  <main class="process-grid">
    <article class="process-card">
      <h2 class="process-title">Pellentesque consequat</h2>
      <div class="process-value">$00.00</div>
      <div class="progress"><div class="progress-fill"></div></div>
      <p class="process-desc">Donec feugiat sed elit eget facilisis. Vivamus vel turpis a tellus ornare rhoncus ut quis quam. Donec eleifend vulputate euismod. Sed varius magna nec enim posuere molestie. Cras ut erat purus. Aliquam pharetra id nisi quis facilisis. Donec dignissim a purus eu pulvinar.</p>
      <div class="process-step"><div class="step-label">Current step :</div><div class="step-name">Executive Negotiation</div></div>
    </article>
    <article class="process-card">
      <h2 class="process-title">Pellentesque consequat</h2>
      <div class="process-value">$00.00</div>
      <div class="progress"><div class="progress-fill"></div></div>
      <p class="process-desc">Donec feugiat sed elit eget facilisis. Vivamus vel turpis a tellus ornare rhoncus ut quis quam. Donec eleifend vulputate euismod. Sed varius magna nec enim posuere molestie. Cras ut erat purus. Aliquam pharetra id nisi quis facilisis. Donec dignissim a purus eu pulvinar.</p>
      <div class="process-step"><div class="step-label">Current step :</div><div class="step-name">Executive Negotiation</div></div>
    </article>
    <article class="process-card">
      <h2 class="process-title">Pellentesque consequat</h2>
      <div class="process-value">$00.00</div>
      <div class="progress"><div class="progress-fill"></div></div>
      <p class="process-desc">Donec feugiat sed elit eget facilisis. Vivamus vel turpis a tellus ornare rhoncus ut quis quam. Donec eleifend vulputate euismod. Sed varius magna nec enim posuere molestie. Cras ut erat purus. Aliquam pharetra id nisi quis facilisis. Donec dignissim a purus eu pulvinar.</p>
      <div class="process-step"><div class="step-label">Current step :</div><div class="step-name">Executive Negotiation</div></div>
    </article>
    <article class="process-card">
      <h2 class="process-title">Pellentesque consequat</h2>
      <div class="process-value">$00.00</div>
      <div class="progress"><div class="progress-fill"></div></div>
      <p class="process-desc">Donec feugiat sed elit eget facilisis. Vivamus vel turpis a tellus ornare rhoncus ut quis quam. Donec eleifend vulputate euismod. Sed varius magna nec enim posuere molestie. Cras ut erat purus. Aliquam pharetra id nisi quis facilisis. Donec dignissim a purus eu pulvinar.</p>
      <div class="process-step"><div class="step-label">Current step :</div><div class="step-name">Executive Negotiation</div></div>
    </article>
    <article class="process-card">
      <h2 class="process-title">Pellentesque consequat</h2>
      <div class="process-value">$00.00</div>
      <div class="progress"><div class="progress-fill"></div></div>
      <p class="process-desc">Donec feugiat sed elit eget facilisis. Vivamus vel turpis a tellus ornare rhoncus ut quis quam. Donec eleifend vulputate euismod. Sed varius magna nec enim posuere molestie. Cras ut erat purus. Aliquam pharetra id nisi quis facilisis. Donec dignissim a purus eu pulvinar.</p>
      <div class="process-step"><div class="step-label">Current step :</div><div class="step-name">Executive Negotiation</div></div>
    </article>
    <article class="process-card">
      <h2 class="process-title">Pellentesque consequat</h2>
      <div class="process-value">$00.00</div>
      <div class="progress"><div class="progress-fill"></div></div>
      <p class="process-desc">Donec feugiat sed elit eget facilisis. Vivamus vel turpis a tellus ornare rhoncus ut quis quam. Donec eleifend vulputate euismod. Sed varius magna nec enim posuere molestie. Cras ut erat purus. Aliquam pharetra id nisi quis facilisis. Donec dignissim a purus eu pulvinar.</p>
      <div class="process-step"><div class="step-label">Current step :</div><div class="step-name">Executive Negotiation</div></div>
    </article>
  </main>

  <footer class="site-footer">Copyright &nbsp;©&nbsp; 2017 &nbsp;Company name. &nbsp;All rights reserved.</footer>
</body>
</html>
```